Flyer-Design für Internethandel auf ausgewählten Marktplätzen
Zielgruppe
Internethandel auf Marktplätzen wie: Verkano, Lumo, Fiska.de, Brix.de
Eigene Webseite: www.talbrunn-laden.de
So ganz festgelegt habe ich mch noch nicht was ich alles im Sortiment haben möchte.
Im Moment besteht der Hauptteil aus Pflaster verschiedenster Sorten, aus verschiedenen Klebebandsorten und aus Werkzeugen wie Cuttermesser und passende Klingen.
Aufgabenstellung
Ich möchte (mit den Farben des Logos ?) einen Flyer, um Käufer darum zu bitten eine bewertung für mich abzugeben.
Soetwas wie: wir sind stets bemüht unsere Service-Leistungen zu verbessern und freuen uns, wenn Sie diese mit einer positven Bewertung honorieren. Siehe angehängtes Bild, das habe ich heute von einem anderen verkäufer bekommen.
Sehr gerne auch einen anderen passenden Text.
Was ich auch gerne hätte, wäre der Hinweis auf unsere Webseite www.talbrunn-laden.de
Dort bieten wir auch Staffelpreise an und Käufer können dadurch sparen wenn Sie mehr kaufen.
Ich habe mal zwei Bilder von Klebebänder mit angehängt. Eventuell können Sie ja auf unserer Internetseite ein Passendes Bild von Klebebandrollen, Pflaster oder Arbeitsschutzmaterial kopieren.
Es ist aber kein muss ein Bild mit ein zu setzen.
Bedruckt werden sollten beide seiten. Größe: Ca. Postkartengröße?!

```html
<!DOCTYPE html>
<html lang="de">
<head>
<meta charset="utf-8">
<title>Talbrunn-Laden – Kundenkarte</title>
<link rel="stylesheet" href="https://fonts.googleapis.com/css2?family=Ubuntu:wght@300;400&family=Italianno&display=swap">
<style>
  :root {
    --backdrop: #c6c6c6;
    --paper: #ffffff;
    --ink: #5a5a5a;
    --brand-green: #4cb848;
    --brand-grey: #5f5f5f;
  }
  * { margin: 0; padding: 0; box-sizing: border-box; }
  html, body { width: 1200px; height: 971px; overflow: hidden; }
  body {
    background: var(--backdrop);
    font-family: "Ubuntu", sans-serif;
    font-weight: 300;
    color: var(--ink);
    position: relative;
  }
  .card {
    position: absolute;
    width: 414px;
    height: 588px;
    background: var(--paper);
    box-shadow: -4px 4px 10px rgba(0,0,0,0.28);
  }
  .card--thanks { left: 172px; top: 238px; }
  .card--offers { left: 614px; top: 153px; }

  .brand {
    position: absolute;
    left: 0; right: 0;
    display: flex;
    justify-content: center;
    align-items: center;
    gap: 10px;
    color: var(--brand-grey);
    font-weight: 400;
    white-space: nowrap;
  }
  .brand__dot { border-radius: 50%; background: var(--brand-green); flex: none; }
  .card--thanks .brand { top: 58px; font-size: 27px; }
  .card--thanks .brand__dot { width: 14px; height: 14px; }
  .card--offers .brand { top: 64px; font-size: 42px; }
  .card--offers .brand__dot { width: 20px; height: 20px; }

  .text { position: absolute; font-size: 13.4px; line-height: 17.5px; }
  .salutation {
    position: absolute; left: 36px; top: 138px;
    font-family: "Italianno", cursive;
    font-size: 30px; color: #4a4a4a;
  }
  .thanks-body { left: 37px; width: 360px; }
  .thanks-body--one { top: 188px; }
  .thanks-body--two { top: 240px; }
  .thanks-body--three { top: 310px; }
  .shop-hint { left: 0; right: 0; top: 415px; text-align: center; }
  .web { position: absolute; left: 0; right: 0; text-align: center; color: var(--brand-green); font-size: 13.4px; }
  .card--thanks .web { top: 486px; }
  .card--offers .web { top: 521px; }

  .tagline {
    position: absolute; left: 58px; top: 160px;
    color: var(--brand-green); font-size: 15px; line-height: 20px;
  }
  .benefit__title {
    position: absolute; left: 58px;
    display: flex; align-items: center; gap: 4px;
    font-size: 13.4px; line-height: 18px;
  }
  .benefit__title svg { width: 18px; height: 18px; flex: none; }
  .benefit__body { left: 58px; width: 300px; }
  .benefit--gift .benefit__title { top: 245px; }
  .benefit--gift .benefit__body { top: 270px; }
  .benefit--bulk .benefit__title { top: 339px; }
  .benefit--bulk .benefit__body { top: 363px; }
  .benefit--shipping .benefit__title { top: 431px; }
  .benefit--shipping .benefit__body { top: 456px; }
</style>
</head>
<body>

<section class="card card--thanks">
  <div class="brand"><span>Talbrunn-Laden</span><span class="brand__dot"></span></div>
  <p class="salutation">Liebe Kunden,</p>
  <p class="text thanks-body thanks-body--one">herzlichen Dank für Ihre Bestellung und Ihr Vertrauen!<br>Wir hoffen, Ihre Erwartungen erfüllt zu haben.</p>
  <p class="text thanks-body thanks-body--two">Unser Bestreben ist es, Ihnen nicht nur einwandfreie<br>Produkte und Leistungen anzubieten, sondern auch<br>unseren Service stets zu verbessern.</p>
  <p class="text thanks-body thanks-body--three">Hierzu benötigen wir Ihr Feedack und freuen uns<br>über Ihre Bewertung – danke!</p>
  <p class="text shop-hint">Kennen Sie schon unseren Online-Shop?<br>Hier finden Sie alle Angebote<br>und attraktive Staffelpreise:</p>
  <p class="web">www.talbrunn-laden.de</p>
</section>

<section class="card card--offers">
  <div class="brand"><span>Talbrunn-Laden</span><span class="brand__dot"></span></div>
  <p class="tagline">Ihr Online-Shop für<br>Verbandstoffe, Wundversorgung<br>Haushalts- und Heimwerkerbedarf</p>

  <div class="benefit benefit--gift">
    <p class="benefit__title"><svg viewBox="0 0 18 18" aria-hidden="true"><circle cx="9" cy="9" r="9" fill="var(--brand-green)"/><path d="M4.5 9.2l3 3.2 6-7" fill="none" stroke="#fff" stroke-width="2.4" stroke-linecap="round" stroke-linejoin="round"/></svg>Gratis-Geschenk</p>
    <p class="text benefit__body">Ein Einkauf bei uns lohnt sich immer, denn zu den unschlagbar günstigen Preisen erhalten Sie bei Ihrem Einkauf ab 15 € ein Gratis-Geschenk.</p>
  </div>

  <div class="benefit benefit--bulk">
    <p class="benefit__title"><svg viewBox="0 0 18 18" aria-hidden="true"><circle cx="9" cy="9" r="9" fill="var(--brand-green)"/><path d="M4.5 9.2l3 3.2 6-7" fill="none" stroke="#fff" stroke-width="2.4" stroke-linecap="round" stroke-linejoin="round"/></svg>Mengenrabatte</p>
    <p class="text benefit__body">Ab 3 Stück bekommen Sie bei uns schon einen attraktiven Mengenrabatt. Kombination mit gleichwertigen Artikeln möglich.</p>
  </div>

  <div class="benefit benefit--shipping">
    <p class="benefit__title"><svg viewBox="0 0 18 18" aria-hidden="true"><circle cx="9" cy="9" r="9" fill="var(--brand-green)"/><path d="M4.5 9.2l3 3.2 6-7" fill="none" stroke="#fff" stroke-width="2.4" stroke-linecap="round" stroke-linejoin="round"/></svg>Sparen Sie sich die Versandkosten</p>
    <p class="text benefit__body">Ab 75 Euro Warenwert übernehmen wir die Versandkosten innerhalb Deutschland für Sie.</p>
  </div>

  <p class="web">www.talbrunn-laden.de</p>
</section>

</body>
</html>
```